Keystone Ledger Solutions, Inc.
I would like to see the back have the faded blue logo like #27.
smaller and centered on the card
address update:
PO Box 2968
Loveland, CO. 80412

```html
<!DOCTYPE html>
<html lang="en">
<head>
<meta charset="utf-8">
<title>Keystone Ledger Solutions, Inc. — Stationery</title>
<link rel="stylesheet" href="https://fonts.googleapis.com/css2?family=Montserrat:wght@700&family=Open+Sans:wght@400;600&display=swap">
<style>
  :root {
    --stage: #2b2d31;
    --paper: #ffffff;
    --paper-shade: #eef1f5;
    --navy: #0e3a86;
    --blue: #1b6fd0;
    --sky: #3d93e8;
    --orange: #f06a1e;
    --ink: #4a4f57;
    --ghost: rgba(27, 111, 208, 0.10);
  }
  * { box-sizing: border-box; margin: 0; padding: 0; }
  html, body { width: 1200px; height: 310px; overflow: hidden; background: var(--stage); }
  .canvas { position: relative; width: 1200px; height: 310px; font-family: "Open Sans", Arial, sans-serif; color: var(--ink); }

  .piece { position: absolute; background: var(--paper); overflow: hidden; box-shadow: 0 3px 8px rgba(0,0,0,.45); }
  .swoosh { position: absolute; left: 0; bottom: 0; width: 100%; }

  .brand { position: absolute; display: flex; align-items: center; gap: 4px; }
  .brand.centered { left: 0; top: 0; width: 100%; height: 100%; justify-content: center; }
  .brand-mark { width: 9px; height: 9px; background: var(--blue); flex: none; }
  .brand-name { font-family: "Montserrat", Arial, sans-serif; font-weight: 700; color: var(--navy); font-size: 6px; line-height: 1.05; letter-spacing: .3px; text-transform: uppercase; white-space: nowrap; }
  .brand.compact { gap: 3px; }
  .brand.compact .brand-mark { width: 7px; height: 7px; }
  .brand.compact .brand-name { font-size: 5px; letter-spacing: .2px; }

  .ghost-mark { position: absolute; display: flex; flex-direction: column; align-items: center; justify-content: center; gap: 4px; }
  .ghost-circle { border-radius: 50%; background: var(--ghost); }
  .ghost-name { font-family: "Montserrat", Arial, sans-serif; font-weight: 700; color: var(--ghost); text-transform: uppercase; text-align: center; line-height: 1.1; white-space: nowrap; }
  .ghost-mark.on-blue .ghost-circle { background: rgba(255,255,255,.12); }
  .ghost-mark.on-blue .ghost-name { color: rgba(255,255,255,.14); }

  .fine { position: absolute; font-size: 3.2px; line-height: 1.45; color: var(--ink); white-space: nowrap; }
  .fine.strong { font-weight: 600; color: var(--navy); }
  .fine.right { text-align: right; }
  .web { position: absolute; font-size: 3.4px; color: var(--blue); font-weight: 600; }

  .card-blue { background: linear-gradient(135deg, var(--sky), var(--navy)); }
  .envelope-back { background: var(--paper-shade); }
  .flap { position: absolute; left: 0; top: 0; width: 100%; height: 100%; }
</style>
</head>
<body>
<main class="canvas">

  <!-- Business card: front -->
  <section class="piece card" style="left:22px;top:30px;width:104px;height:58px">
    <div class="brand compact" style="left:6px;top:6px">
      <span class="brand-mark"></span>
      <span class="brand-name">Keystone Ledger<br>Solutions, Inc.</span>
    </div>
    <p class="fine strong" style="left:6px;top:24px">Jordan Reyes</p>
    <p class="fine" style="left:6px;top:29px">Account Manager</p>
    <p class="fine right" style="right:6px;top:24px">PO Box 2968<br>Loveland, CO. 80412<br>Tel 970.555.0142</p>
    <svg class="swoosh" viewBox="0 0 100 20" preserveAspectRatio="none" style="height:14px">
      <path d="M0 12 Q50 2 100 8 L100 20 L0 20Z" fill="var(--blue)"/>
      <path d="M0 10 Q50 0 100 6" fill="none" stroke="var(--orange)" stroke-width="1"/>
    </svg>
  </section>

  <!-- Business card: back, faded mark centered -->
  <section class="piece card" style="left:19px;top:122px;width:118px;height:64px">
    <div class="ghost-mark" style="left:0;top:0;width:100%;height:100%">
      <span class="ghost-circle" style="width:26px;height:26px"></span>
      <span class="ghost-name" style="font-size:5px">Keystone Ledger Solutions</span>
    </div>
  </section>

  <!-- Business card: back, brand centered -->
  <section class="piece card" style="left:149px;top:122px;width:118px;height:64px">
    <div class="brand centered">
      <span class="brand-mark"></span>
      <span class="brand-name">Keystone Ledger<br>Solutions, Inc.</span>
    </div>
  </section>

  <!-- Business card: front variant -->
  <section class="piece card" style="left:19px;top:212px;width:118px;height:66px">
    <div class="brand" style="left:7px;top:7px">
      <span class="brand-mark"></span>
      <span class="brand-name">Keystone Ledger<br>Solutions, Inc.</span>
    </div>
    <p class="web" style="left:7px;top:44px">www.klsinc.com</p>
    <svg class="swoosh" viewBox="0 0 100 20" preserveAspectRatio="none" style="height:12px">
      <path d="M0 14 Q60 4 100 10 L100 20 L0 20Z" fill="var(--blue)"/>
      <path d="M0 12 Q60 2 100 8" fill="none" stroke="var(--orange)" stroke-width="1"/>
    </svg>
  </section>

  <!-- Business card: blue back -->
  <section class="piece card card-blue" style="left:149px;top:212px;width:118px;height:66px">
    <div class="ghost-mark on-blue" style="left:0;top:0;width:100%;height:100%">
      <span class="ghost-circle" style="width:28px;height:28px"></span>
      <span class="ghost-name" style="font-size:5px">Keystone Ledger Solutions</span>
    </div>
  </section>

  <!-- Letterhead: first page -->
  <section class="piece letterhead" style="left:274px;top:24px;width:202px;height:260px">
    <div class="brand" style="left:14px;top:12px">
      <span class="brand-mark"></span>
      <span class="brand-name">Keystone Ledger<br>Solutions, Inc.</span>
    </div>
    <p class="fine" style="left:128px;top:12px">PO Box 2968<br>Loveland, CO. 80412<br>Tel 970.555.0142<br>info@klsinc.com</p>
    <div class="ghost-mark" style="left:51px;top:90px;width:100px;height:100px">
      <span class="ghost-circle" style="width:60px;height:60px"></span>
    </div>
    <svg class="swoosh" viewBox="0 0 100 20" preserveAspectRatio="none" style="height:22px">
      <path d="M0 12 Q55 0 100 10 L100 20 L0 20Z" fill="var(--blue)"/>
      <path d="M0 10 Q55 -2 100 8" fill="none" stroke="var(--orange)" stroke-width=".8"/>
    </svg>
  </section>

  <!-- Letterhead: second page -->
  <section class="piece letterhead" style="left:492px;top:24px;width:204px;height:260px">
    <div class="brand" style="left:14px;top:12px">
      <span class="brand-mark"></span>
      <span class="brand-name">Keystone Ledger<br>Solutions, Inc.</span>
    </div>
    <div class="ghost-mark" style="left:52px;top:90px;width:100px;height:100px">
      <span class="ghost-circle" style="width:60px;height:60px"></span>
    </div>
    <svg class="swoosh" viewBox="0 0 100 20" preserveAspectRatio="none" style="height:22px">
      <path d="M0 12 Q55 0 100 10 L100 20 L0 20Z" fill="var(--blue)"/>
      <path d="M0 10 Q55 -2 100 8" fill="none" stroke="var(--orange)" stroke-width=".8"/>
    </svg>
  </section>

  <!-- Envelope: front -->
  <section class="piece envelope" style="left:710px;top:43px;width:226px;height:137px">
    <div class="brand" style="left:12px;top:12px">
      <span class="brand-mark"></span>
      <span class="brand-name">Keystone Ledger<br>Solutions, Inc.</span>
    </div>
    <p class="fine" style="left:12px;top:30px">PO Box 2968<br>Loveland, CO. 80412</p>
    <svg class="swoosh" viewBox="0 0 100 20" preserveAspectRatio="none" style="height:26px">
      <path d="M0 10 Q55 0 100 8 L100 20 L0 20Z" fill="var(--blue)"/>
      <path d="M0 8 Q55 -2 100 6" fill="none" stroke="var(--orange)" stroke-width=".8"/>
    </svg>
  </section>

  <!-- Envelope: window / faded mark -->
  <section class="piece envelope" style="left:710px;top:192px;width:226px;height:91px">
    <div class="ghost-mark" style="left:150px;top:6px;width:60px;height:60px">
      <span class="ghost-circle" style="width:44px;height:44px"></span>
    </div>
    <svg class="swoosh" viewBox="0 0 100 20" preserveAspectRatio="none" style="height:18px">
      <path d="M0 10 Q55 0 100 8 L100 20 L0 20Z" fill="var(--blue)"/>
      <path d="M0 8 Q55 -2 100 6" fill="none" stroke="var(--orange)" stroke-width=".8"/>
    </svg>
  </section>

  <!-- Envelope: orange flap -->
  <section class="piece envelope-back" style="left:950px;top:60px;width:226px;height:88px">
    <svg class="flap" viewBox="0 0 100 40" preserveAspectRatio="none">
      <path d="M0 0 H100 V10 L50 26 L0 10Z" fill="var(--orange)"/>
      <path d="M0 10 L50 26 L100 10" fill="none" stroke="var(--blue)" stroke-width="1.2"/>
    </svg>
  </section>

  <!-- Envelope: back with blue seal -->
  <section class="piece envelope-back" style="left:950px;top:120px;width:226px;height:96px">
    <svg class="flap" viewBox="0 0 100 40" preserveAspectRatio="none">
      <path d="M0 0 L50 22 L100 0" fill="var(--paper)" stroke="#c9d0da" stroke-width=".4"/>
      <path d="M0 40 L40 20 M100 40 L60 20" stroke="#d4dae2" stroke-width=".4"/>
    </svg>
    <div class="ghost-mark" style="left:93px;top:38px;width:40px;height:40px">
      <span class="ghost-circle" style="width:26px;height:26px;background:var(--blue)"></span>
    </div>
  </section>

  <!-- Envelope: plain back -->
  <section class="piece envelope-back" style="left:950px;top:187px;width:226px;height:96px">
    <svg class="flap" viewBox="0 0 100 40" preserveAspectRatio="none">
      <path d="M0 0 L50 22 L100 0" fill="var(--paper)" stroke="#c9d0da" stroke-width=".4"/>
      <path d="M0 40 L40 20 M100 40 L60 20" stroke="#d4dae2" stroke-width=".4"/>
    </svg>
  </section>

</main>
</body>
</html>
```